Company Values Graphic

We are looking for a design of our company values that can be used in a variety of places including our website, mousepads, office posters, business cards, etc.

Notes:
- We'd rather have icons/art than photographs on the poster.... so more like an infographic
- The core value group headings are not required, but can be included if you think grouping the values works for your design
- We have a logo for our software product but that logo is not required
- We don't need/want clever images to accompany each value, but some images are fine
- BrisKel logo attached
- BrisKel colors are attached
- BrisKel logo is Nunito Sans ExtraBold 800
- BrisKel website uses Roboto

Our Values - Who we will work with (and who we will not)
The right set of values are essential to building and maintaining a culture that we all wake up eager to be a part of each day. They are foundational to all hiring and firing decisions. They attract the right people and repel the wrong ones.

BE HELPFUL
Make every person and place better because you are there.
Deliver wow with every interaction.

BE HUMBLE
Listen with every muscle.
Passionately help others first.
Seek first to understand.

BE HONEST
Earn trust every day.
Be open and direct.
Treat everyone with fairness and respect.

BE HUMAN
Celebrate passion and action.
Create an environment where people are authentic.
Hire great people and expect a lot from them

BE COURAGEOUS
Dare mighty things.
Make and honor commitments.
All great things start with a small act of courage applied at the right moment.

```html
<!DOCTYPE html>
<html lang="en">
<head>
<meta charset="utf-8">
<title>Our Values – Who we will work with</title>
<link href="https://fonts.googleapis.com/css2?family=Nunito+Sans:wght@800;900&family=Roboto:wght@400&display=swap" rel="stylesheet">
<style>
  :root {
    --backdrop: #333333;
    --paper: #ffffff;
    --panel-grey: #e8e9eb;
    --brand-red: #ed1f28;
    --brand-orange: #f79c21;
    --ink: #0a0a0a;
    --tick: #f15a24;
  }
  * { margin: 0; padding: 0; box-sizing: border-box; }
  html, body { width: 1200px; height: 1200px; overflow: hidden; background: var(--backdrop); }
  .poster {
    position: absolute; left: 225px; top: 74px; width: 750px; height: 1051px;
    background: var(--paper); overflow: hidden;
    box-shadow: 0 4px 18px rgba(0,0,0,.35);
  }
  .side-panel {
    position: absolute; left: 0; top: 0; width: 209px; height: 1051px;
    background: var(--panel-grey);
    border-bottom-right-radius: 70px 200px;
  }
  .header-shapes { position: absolute; left: 0; top: 0; width: 750px; height: 260px; }
  .vertical-title {
    position: absolute; width: 960px; height: 160px;
    left: calc(92px - 480px); top: calc(552px - 80px);
    transform: rotate(-90deg);
    font-family: "Nunito Sans", sans-serif; font-weight: 900;
    font-size: 165px; line-height: 160px; color: var(--ink);
    white-space: nowrap; text-align: center; letter-spacing: -1px;
  }
  .headline {
    position: absolute; right: 23px; top: 16px; text-align: right;
    font-family: "Nunito Sans", sans-serif; font-weight: 800; color: var(--ink);
  }
  .headline .main { font-size: 34px; line-height: 42px; display: block; }
  .headline .sub { font-size: 23px; line-height: 30px; display: block; }
  .intro {
    position: absolute; right: 23px; top: 99px; width: 520px; text-align: right;
    font-family: "Roboto", sans-serif; font-size: 14.8px; line-height: 18.6px; color: var(--paper);
  }
  .timeline {
    position: absolute; left: 276px; top: 272px; height: 760px; width: 0;
    border-left: 2px dotted var(--ink);
  }
  .value-icon {
    position: absolute; left: 248px; width: 58px; height: 58px; border-radius: 50%;
    background: var(--brand-orange);
  }
  .value {
    position: absolute; left: 324px; width: 410px;
    font-family: "Nunito Sans", sans-serif; color: var(--ink);
  }
  .value .prefix { font-weight: 900; font-size: 22px; line-height: 22px; display: block; }
  .value .name { font-weight: 900; font-size: 32px; line-height: 38px; display: block; letter-spacing: .3px; }
  .value ul { list-style: none; margin-top: 6px; }
  .value li {
    font-family: "Roboto", sans-serif; font-size: 14.8px; line-height: 23.5px;
    display: flex; align-items: flex-start; gap: 7px;
  }
  .value li svg { flex: none; width: 10px; height: 10px; margin-top: 7px; }
  .value li span { line-height: 18.5px; padding: 2.5px 0; }
</style>
</head>
<body>
<div class="poster">
  <div class="side-panel"></div>

  <svg class="header-shapes" viewBox="0 0 750 260" aria-hidden="true">
    <path d="M123,0 C130,110 230,190 370,190 L640,190 C700,190 735,215 750,235 L750,0 Z"
          fill="var(--brand-red)" stroke="var(--paper)" stroke-width="8"/>
    <path d="M123,0 C130,110 230,190 370,190 L640,190 C700,190 735,215 750,235 L750,0 Z"
          fill="var(--brand-red)"/>
    <path d="M269,0 C310,60 370,94 460,94 L680,94 C715,94 735,100 750,110 L750,0 Z"
          fill="var(--brand-orange)"/>
  </svg>

  <h1 class="vertical-title">Our Values -</h1>

  <h2 class="headline">
    <span class="main">Who we will work with</span>
    <span class="sub">(and who we will not)</span>
  </h2>

  <p class="intro">The right set of values are essential to building and maintaining a culture that<br>we all wake up eager to be a part of each day. They are foundational to all<br>hiring and firing decisions. They attract the right people and<br>repel the wrong ones.</p>

  <div class="timeline"></div>

  <div class="value-icon" style="top:213px" role="img" aria-label="Helping hands icon"></div>
  <div class="value-icon" style="top:362px" role="img" aria-label="Head with heart icon"></div>
  <div class="value-icon" style="top:529px" role="img" aria-label="Star held in hand icon"></div>
  <div class="value-icon" style="top:699px" role="img" aria-label="Group of people icon"></div>
  <div class="value-icon" style="top:870px" role="img" aria-label="Raised fist icon"></div>

  <section class="value" style="top:217px">
    <span class="prefix">BE</span><span class="name">HELPFUL</span>
    <ul>
      <li><svg viewBox="0 0 10 10"><circle cx="5" cy="5" r="4.2" fill="none" stroke="var(--tick)" stroke-width="1"/><path d="M3 5.2 4.5 6.6 7.2 3.6" fill="none" stroke="var(--tick)" stroke-width="1.1"/></svg><span>Make every person and place better because you are there.</span></li>
      <li><svg viewBox="0 0 10 10"><circle cx="5" cy="5" r="4.2" fill="none" stroke="var(--tick)" stroke-width="1"/><path d="M3 5.2 4.5 6.6 7.2 3.6" fill="none" stroke="var(--tick)" stroke-width="1.1"/></svg><span>Deliver wow with every interaction.</span></li>
    </ul>
  </section>

  <section class="value" style="top:366px">
    <span class="prefix">BE</span><span class="name">HUMBLE</span>
    <ul>
      <li><svg viewBox="0 0 10 10"><circle cx="5" cy="5" r="4.2" fill="none" stroke="var(--tick)" stroke-width="1"/><path d="M3 5.2 4.5 6.6 7.2 3.6" fill="none" stroke="var(--tick)" stroke-width="1.1"/></svg><span>Listen with every muscle.</span></li>
      <li><svg viewBox="0 0 10 10"><circle cx="5" cy="5" r="4.2" fill="none" stroke="var(--tick)" stroke-width="1"/><path d="M3 5.2 4.5 6.6 7.2 3.6" fill="none" stroke="var(--tick)" stroke-width="1.1"/></svg><span>Passionately help others first.</span></li>
      <li><svg viewBox="0 0 10 10"><circle cx="5" cy="5" r="4.2" fill="none" stroke="var(--tick)" stroke-width="1"/><path d="M3 5.2 4.5 6.6 7.2 3.6" fill="none" stroke="var(--tick)" stroke-width="1.1"/></svg><span>Seek first to understand.</span></li>
    </ul>
  </section>

  <section class="value" style="top:534px">
    <span class="prefix">BE</span><span class="name">HONEST</span>
    <ul>
      <li><svg viewBox="0 0 10 10"><circle cx="5" cy="5" r="4.2" fill="none" stroke="var(--tick)" stroke-width="1"/><path d="M3 5.2 4.5 6.6 7.2 3.6" fill="none" stroke="var(--tick)" stroke-width="1.1"/></svg><span>Earn trust every day.</span></li>
      <li><svg viewBox="0 0 10 10"><circle cx="5" cy="5" r="4.2" fill="none" stroke="var(--tick)" stroke-width="1"/><path d="M3 5.2 4.5 6.6 7.2 3.6" fill="none" stroke="var(--tick)" stroke-width="1.1"/></svg><span>Be open and direct.</span></li>
      <li><svg viewBox="0 0 10 10"><circle cx="5" cy="5" r="4.2" fill="none" stroke="var(--tick)" stroke-width="1"/><path d="M3 5.2 4.5 6.6 7.2 3.6" fill="none" stroke="var(--tick)" stroke-width="1.1"/></svg><span>Treat everyone with fairness and respect.</span></li>
    </ul>
  </section>

  <section class="value" style="top:709px">
    <span class="prefix">BE</span><span class="name">HUMAN</span>
    <ul>
      <li><svg viewBox="0 0 10 10"><circle cx="5" cy="5" r="4.2" fill="none" stroke="var(--tick)" stroke-width="1"/><path d="M3 5.2 4.5 6.6 7.2 3.6" fill="none" stroke="var(--tick)" stroke-width="1.1"/></svg><span>Celebrate passion and action.</span></li>
      <li><svg viewBox="0 0 10 10"><circle cx="5" cy="5" r="4.2" fill="none" stroke="var(--tick)" stroke-width="1"/><path d="M3 5.2 4.5 6.6 7.2 3.6" fill="none" stroke="var(--tick)" stroke-width="1.1"/></svg><span>Create an environment where people are authentic.</span></li>
      <li><svg viewBox="0 0 10 10"><circle cx="5" cy="5" r="4.2" fill="none" stroke="var(--tick)" stroke-width="1"/><path d="M3 5.2 4.5 6.6 7.2 3.6" fill="none" stroke="var(--tick)" stroke-width="1.1"/></svg><span>Hire great people and expect a lot from them.</span></li>
    </ul>
  </section>

  <section class="value" style="top:881px">
    <span class="prefix">BE</span><span class="name">COURAGEOUS</span>
    <ul>
      <li><svg viewBox="0 0 10 10"><circle cx="5" cy="5" r="4.2" fill="none" stroke="var(--tick)" stroke-width="1"/><path d="M3 5.2 4.5 6.6 7.2 3.6" fill="none" stroke="var(--tick)" stroke-width="1.1"/></svg><span>Dare mighty things.</span></li>
      <li><svg viewBox="0 0 10 10"><circle cx="5" cy="5" r="4.2" fill="none" stroke="var(--tick)" stroke-width="1"/><path d="M3 5.2 4.5 6.6 7.2 3.6" fill="none" stroke="var(--tick)" stroke-width="1.1"/></svg><span>Make and honor commitments.</span></li>
      <li><svg viewBox="0 0 10 10"><circle cx="5" cy="5" r="4.2" fill="none" stroke="var(--tick)" stroke-width="1"/><path d="M3 5.2 4.5 6.6 7.2 3.6" fill="none" stroke="var(--tick)" stroke-width="1.1"/></svg><span>All great things start with a small act of courage applied<br>at the right moment.</span></li>
    </ul>
  </section>
</div>
</body>
</html>
```